What makes us Different Managed Communications Services Provider Flyer

We need a flyer to explain why we are different than other "managed IT services" company. Gives a brief description of our company and services that can entice clients and potential clients to setup a FREE consultation with us. This will become part of an ongoing marketing campaign that includes emails, leave behinds, brochures, and more

```html
<!DOCTYPE html>
<html lang="en">
<head>
<meta charset="utf-8">
<title>Northline Voice &amp; Data – Trifold Brochure</title>
<link href="https://fonts.googleapis.com/css2?family=Manrope:wght@400;500;700;800&display=swap" rel="stylesheet">
<style>
:root{
  --bg:#e4e4e4;
  --paper:#f4f5f6;
  --ink:#1b1b1d;
  --muted:#3a3a3e;
  --blue:#1f57cf;
  --blue-deep:#0b2fa6;
  --navy:#0c1a4a;
  --black:#151515;
  --white:#ffffff;
  --rule:#c9ccd2;
}
*{box-sizing:border-box;margin:0;padding:0}
html,body{width:843px;height:1200px;overflow:hidden;background:var(--bg)}
body{font-family:"Manrope",Arial,sans-serif;color:var(--ink);position:relative}
.sheet{position:absolute;left:20px;width:803px;height:570px;display:grid;grid-template-columns:repeat(3,1fr);background:var(--paper);box-shadow:0 10px 22px rgba(0,0,0,.18);overflow:hidden}
.sheet--outside{top:20px}
.sheet--inside{top:610px}
.panel{position:relative;overflow:hidden;border-right:1px solid #dcdfe3}
.panel:last-child{border-right:none}
.photo{position:absolute;left:0;width:100%}
.accent{display:block;width:34px;height:4px;background:var(--blue-deep);margin-bottom:8px}
.heading{font-size:15px;line-height:1.15;font-weight:400}
.heading b{font-weight:800}
.body-text{font-size:7.1px;line-height:1.6;color:var(--muted)}
.body-text b{font-weight:700;color:var(--ink)}
.body-text + .body-text{margin-top:9px}
.copy{position:absolute;left:24px;right:22px}

/* outside */
.contact-label{font-size:6px;font-weight:800;letter-spacing:.04em;margin-top:11px}
.contact-value{font-size:8px;line-height:1.4}
.cover-band{position:absolute;left:0;right:0;top:318px;bottom:0;background:var(--blue)}
.cover-strip{position:absolute;left:0;bottom:0;width:26px;height:150px;background:var(--navy)}
.cover-title{position:absolute;left:44px;right:18px;top:352px;color:var(--white);font-size:20px;line-height:1.12;font-weight:400}
.cover-title b{font-weight:800}
.cover-tag{position:absolute;left:44px;top:438px;color:var(--white);font-size:8.5px;letter-spacing:.03em}
.cover-rule{position:absolute;left:44px;right:20px;top:460px;height:2px;background:var(--white)}
.cover-phone{position:absolute;left:44px;top:476px;color:var(--white);font-size:10.5px;font-weight:700}

/* inside */
.spread-photo{position:absolute;top:0;left:436px;width:367px;height:262px;background:linear-gradient(135deg,#c9ccd0 0%,#7d828a 45%,#2c3038 100%);z-index:1}
.callout{position:absolute;left:293px;top:166px;width:233px;height:96px;background:var(--blue);color:var(--white);padding:11px 14px;font-size:7.2px;line-height:1.55;z-index:2}
.services{position:absolute;left:24px;right:22px;top:280px;list-style:none}
.service{display:flex;gap:10px;align-items:flex-start;padding:9px 0 10px;border-bottom:1px solid var(--rule);font-size:6.8px;line-height:1.5;color:var(--muted)}
.service:last-child{border-bottom:none}
.service b{color:var(--ink);font-weight:700}
.service svg{flex:0 0 22px;width:22px;height:22px}
.base-rule{position:absolute;left:24px;top:519px;width:487px;height:2.5px;background:var(--blue-deep);z-index:2}
.base-text{position:absolute;top:533px;font-size:9px;font-weight:800;white-space:nowrap}
.base-text--web{font-size:7.2px;letter-spacing:.08em;top:535px}
.panel--dark{background:var(--black)}
.panel--dark .heading,.panel--dark .body-text,.panel--dark .body-text b{color:#eaeaea}
</style>
</head>
<body>

<section class="sheet sheet--outside">
  <div class="panel">
    <div class="photo" style="top:0;height:240px;background:linear-gradient(135deg,#d8dadc 0%,#c4c2bf 40%,#6e6f74 75%,#3f4148 100%)" role="img" aria-label="Photo of a smiling professional working at a laptop in a bright office"></div>
    <div class="copy" style="top:262px">
      <span class="accent"></span>
      <h2 class="heading"><b>Our Clients Stay</b> Because We Deliver</h2>
      <p class="body-text" style="margin-top:12px">For over 40 years, we have maintained a standard of excellence that <b>other companies simply cannot compare with.</b> Our team of experts consistently goes above and beyond, ensuring that clients not only <b>get the support they need but also receive the strategic guidance necessary to stay ahead in an ever-evolving digital landscape.</b></p>
      <p class="body-text">Our <b>90-day performance</b> review process ensures that we continuously improve our service based on client feedback. This process allows us to <b>adapt, refine, and enhance our approach,</b> providing a truly personalized IT experience that aligns with business objectives.</p>
    </div>
  </div>

  <div class="panel">
    <div class="copy" style="top:36px">
      <span class="accent"></span>
      <h2 class="heading">A Legacy of <b>Trust &amp; Reliability</b></h2>
      <p class="body-text" style="margin-top:14px">The fact that many of our clients have remained with us for <b>decades without a formal contract</b> speaks volumes about the trust we have built. We don't lock in clients with paperwork—we keep them with results. <b>That's the difference between a standard managed IT provider and an IT partner who genuinely cares.</b></p>
      <p class="body-text">If you're looking for an IT provider that will treat your business as if it were their own, look no further. Our legacy of service, innovation, and commitment to our clients is what sets us apart from the rest.</p>
    </div>
    <div class="copy" style="top:330px">
      <span class="accent"></span>
      <h2 class="heading"><b>Contact</b> Us</h2>
      <p class="contact-label" style="margin-top:18px">ADDRESS</p>
      <p class="contact-value">2200 Meridian Park Dr,<br>Austin, TX 78701</p>
      <p class="contact-label">PHONE</p>
      <p class="contact-value">(555) 014-2288</p>
      <p class="contact-label">WEBSITE</p>
      <p class="contact-value">www.northlinevoicedata.com</p>
    </div>
  </div>

  <div class="panel">
    <div class="photo" style="top:0;height:318px;background:linear-gradient(160deg,#2b2d31 0%,#55585e 45%,#1b1c1f 100%)" role="img" aria-label="Photo of a network server rack with patch cables"></div>
    <div class="cover-band"></div>
    <div class="cover-strip"></div>
    <h1 class="cover-title">More Than Just a <b>Managed IT Provider</b></h1>
    <p class="cover-tag">OUR LEGACY OF EXCELLENCE</p>
    <div class="cover-rule"></div>
    <p class="cover-phone">(555) 014-2288</p>
  </div>
</section>

<section class="sheet sheet--inside">
  <div class="panel">
    <div class="photo" style="top:23px;height:239px;background:linear-gradient(135deg,#0e3fb8 0%,#2f7de8 45%,#8fb8f0 75%,#dfe7f3 100%)" role="img" aria-label="Photo of blue network cables plugged into a switch"></div>
    <div class="copy" style="top:280px">
      <span class="accent"></span>
      <h2 class="heading" style="font-weight:800">Northline Voice &amp; Data</h2>
      <p class="body-text" style="margin-top:24px">At our company, we are far more than your typical managed IT provider. Since our founding in 1983, we have built a reputation based on trust, reliability, and unparalleled service. With <b>client relationships spanning 20 to 30 years,</b> we have demonstrated a level of commitment that few IT firms can match. What sets us apart is not just our technical expertise but the <b>deep, long-term partnerships</b> we cultivate with our clients—many of whom have stayed with us <b>without ever being locked into a contract.</b> That is a testament to the exceptional quality of our service and the trust we have earned over decades.</p>
    </div>
    <p class="base-text" style="left:24px">(555) 014-2288</p>
  </div>

  <div class="panel">
    <div class="copy" style="top:24px;right:100px">
      <span class="accent"></span>
      <h2 class="heading"><b>A Holistic Approach</b> to IT Management</h2>
    </div>
    <ul class="services">
      <li class="service">
        <svg viewBox="0 0 24 24" fill="none" stroke="#1f57cf" stroke-width="1.3"><rect x="2" y="5" width="16" height="15" rx="1"/><path d="M5 16l4-4 3 2 4-5"/><circle cx="19" cy="6" r="3"/></svg>
        <span><b>Strategic IT Roadmaps</b> customized to drive business growth.</span>
      </li>
      <li class="service">
        <svg viewBox="0 0 24 24" fill="none" stroke="#1f57cf" stroke-width="1.3"><circle cx="12" cy="12" r="6"/><rect x="9.5" y="11" width="5" height="4"/><path d="M10.5 11V9.5a1.5 1.5 0 013 0V11M2 6h4M2 18h4M18 6h4M18 18h4M6 6l2 2M6 18l2-2M18 6l-2 2M18 18l-2-2"/></svg>
        <span><b>Proactive cybersecurity assessments</b> that help keep businesses secure.</span>
      </li>
      <li class="service">
        <svg viewBox="0 0 24 24" fill="none" stroke="#1f57cf" stroke-width="1.3"><path d="M7 10a4 4 0 018-1 3 3 0 012 5H7a2.5 2.5 0 010-5z"/><rect x="4" y="15" width="16" height="7"/><path d="M12 12v6"/></svg>
        <span><b>Comprehensive backup and disaster recovery solutions</b> that provide peace of mind.</span>
      </li>
      <li class="service">
        <svg viewBox="0 0 24 24" fill="none" stroke="#1f57cf" stroke-width="1.3"><path d="M4 13v-2a8 8 0 0116 0v2"/><rect x="2.5" y="12" width="4" height="6" rx="1"/><rect x="17.5" y="12" width="4" height="6" rx="1"/><path d="M19.5 18c0 2-2 3-5 3"/><path d="M9 13h6"/></svg>
        <span><b>Industry-leading response times</b> and dedicated support teams focused on delivering an exceptional client experience.</span>
      </li>
    </ul>
    <p class="base-text base-text--web" style="left:24px">www.northlinevoicedata.com</p>
  </div>

  <div class="panel panel--dark">
    <div class="copy" style="top:280px">
      <span class="accent"></span>
      <h2 class="heading"><b>Our Clients Stay</b> Because We Deliver</h2>
      <p class="body-text" style="margin-top:18px">For over 40 years, we have maintained a standard of excellence that <b>other companies simply cannot compare with.</b> Our team of experts consistently goes above and beyond, ensuring that clients not only <b>get the support they need</b> but also receive the strategic guidance necessary to stay ahead in an ever-evolving digital landscape.</p>
      <p class="body-text">Our 90-day performance review process ensures that we continuously improve our service based on client feedback. This process allows us to adapt, refine, and enhance our approach, providing a truly personalized IT experience that aligns with business objectives.</p>
    </div>
  </div>

  <div class="spread-photo" role="img" aria-label="Photo of an IT technician working at a multi-monitor desk"></div>
  <p class="callout">We don't just manage IT—we integrate ourselves into your business, ensuring that technology aligns with your strategic goals. Our services go beyond traditional break-fix support. we offer</p>
  <div class="base-rule"></div>
</section>

</body>
</html>
```